Webdesign für Birke Werkstatt
Zielgruppe
Birke Werkstatt produziert GfK Formteile und Abdeckungen
Einzelanfertigungen • Negativ - Formenbau • Prototyping • Ur-Modellbau
Formteile • Abdeckungen • Behälter • Sonderanfertigungen • Beschichtungen
Prototypen Modellbau • Anfertigung von Negativformen • Reparaturen • Fahrzeugteile
Hauptzielgruppe ist die Luftfahrtindustrie (Abdeckungen für Triebwerke)
Durch den Prototypenbau und die Einzelanfertigungen ist die Zielgruppe nicht klar zu definieren. Es werden Einzelteile jeglicher Art aus GfK hergestellt.
Dies können auch Anbauteile für PKW, Poolbeschichtungen, Teile für Boote etc sein.
Es gibt auch Kleinserien. Beispielsweise baut Birke-Werkstatt Motorhauben für Hallo-Brenner Rasenmähertrecker aus den 70er Jahren nach, die es nicht mehr zu kaufen gibt.
Aufgabenstellung
Der Designer hat alle Freiheiten. Die Seite muss natürlich responsiv funktionieren.
Außer dem Logo gibt es keine must-haves.
Schriftart aus dem Logo: EXO 2

```html
<!DOCTYPE html>
<html lang="de">
<head>
<meta charset="utf-8">
<title>Birke Werkstatt – GfK Formteile</title>
<link href="https://fonts.googleapis.com/css2?family=Exo+2:wght@300;400;500;600;700;800&display=swap" rel="stylesheet">
<style>
:root{
  --blue:#1b5a8c;
  --blue-dark:#174e7a;
  --blue-mid:#2b6ca3;
  --band:#5b93c6;
  --text:#3a4450;
  --muted:#6f7d8a;
  --footer:#f0f3f6;
  --white:#fff;
}
*{box-sizing:border-box;margin:0;padding:0}
html,body{width:788px;height:1200px;overflow:hidden;background:#fff}
body{font-family:"Exo 2",sans-serif;color:var(--text)}
.page{position:relative;width:1440px;height:2192px;transform:scale(0.54722);transform-origin:0 0}
.abs{position:absolute}
a{color:inherit;text-decoration:none}

/* header */
.header-shape{position:absolute;left:0;top:0}
.brand{left:92px;top:22px;display:flex;align-items:center;gap:14px}
.brand-mark{width:78px;height:78px;border-radius:50%;border:3px solid var(--blue)}
.brand-name{font-size:34px;font-weight:700;color:var(--blue);line-height:1}
.brand-tag{font-size:10px;color:var(--muted);margin-top:6px}
.phone-top{left:470px;top:9px;color:var(--blue);font-size:13px;line-height:1.2}
.phone-top b{font-size:10px;font-weight:600;display:block}
.meta{right:92px;top:17px;font-size:12px;color:var(--muted);display:flex;gap:8px;align-items:center}
.meta .flag{width:20px;height:12px;background:linear-gradient(#222 33%,#d32 33% 66%,#fc0 66%)}
.meta .lnk{color:var(--blue)}
.meta strong{color:var(--blue);font-weight:600}
.nav{left:470px;top:69px;display:flex;gap:0;font-size:14px;color:#fff}
.nav a{padding:9px 18px;height:36px;display:block}
.nav a.active{background:#fff;color:var(--blue);font-weight:700;padding:9px 12px}

/* hero */
.hero{left:0;top:125px;width:1440px;height:430px;background:linear-gradient(100deg,#3c5268 0%,#6f8497 35%,#a9b6c1 60%,#8b99a6 80%,#5c6b78 100%)}
.hero-title{left:91px;top:172px;color:#fff}
.hero-title .l1{font-size:27px;font-weight:400}
.hero-title .l1 b{font-size:40px;font-weight:800}
.hero-title .l2{font-size:25px;line-height:1.1}
.hero-title .l3{font-size:15px;font-weight:500;color:#dfe6ee}
.hero-btn{left:91px;top:289px;width:269px;height:50px;background:#fff;color:var(--blue);font-weight:700;font-size:15px;display:flex;align-items:center;gap:12px;padding-left:14px;clip-path:polygon(0 0,100% 0,98% 100%,0 100%)}
.dots{left:25px;top:294px;display:flex;flex-direction:column;gap:5px}
.dots i{width:8px;height:8px;border-radius:50%;background:#cfd6dd;display:block}
.dots i.on{width:12px;height:12px;margin-left:-2px;border:2px solid #fff;background:#cfd6dd}
.arrows{left:1340px;top:499px;display:flex;gap:2px}
.arrows span{width:30px;height:30px;background:rgba(255,255,255,.6);display:flex;align-items:center;justify-content:center;color:var(--blue)}
.arrows span+span{background:#fff}
.submenu{left:627px;top:125px;width:246px;background:var(--blue);color:#fff;font-size:13px}
.submenu .head{font-size:10px;font-weight:600;color:#9dbad5;padding:0 19px;height:16px;line-height:14px}
.submenu a{display:flex;justify-content:space-between;padding:0 19px;height:40px;align-items:center;border-top:1px solid rgba(255,255,255,.15)}
.submenu a:first-of-type{border-top:0;height:33px}

/* intro */
.intro{left:0;top:593px;width:1440px;text-align:center}
.intro h2{font-size:30px;font-weight:700;color:var(--blue)}
.intro .sub{font-size:17px;color:var(--blue)}
.intro p{font-size:13px;width:840px;margin:26px auto 0;line-height:1.35}
.step{width:300px;text-align:center;top:767px}
.step .ico{position:relative;height:84px;margin-bottom:20px}
.step .num{position:absolute;top:0;width:30px;height:30px;background:var(--blue);color:#fff;font-size:13px;font-weight:700;display:flex;align-items:center;justify-content:center}
.step h3{font-size:24px;font-weight:700;color:var(--blue)}
.step .tag{font-size:13px;color:var(--blue-mid);margin-top:4px}
.step p{font-size:13px;line-height:1.32;margin-top:10px}
.btn-dark{background:var(--blue);color:#fff;display:flex;align-items:center;font-weight:700;clip-path:polygon(1% 0,100% 0,99% 100%,0 100%)}
.about-btn{left:586px;top:1037px;width:268px;height:50px;padding:0 22px;font-size:15px}
.about-btn small{font-weight:400;font-size:11px;margin-left:auto;margin-right:16px}

/* trust band */
.band{left:0;top:1137px;width:1440px;height:338px;background:linear-gradient(90deg,#4f8ac0,#6aa0d0 45%,#5a92c5 75%,#4a84b9)}
.band-title{left:166px;top:1196px;color:#fff;font-size:35px;line-height:1.1;font-weight:400}
.band-title b{font-size:42px;font-weight:800}
.band-text{left:166px;top:1296px;width:620px;color:#fff;font-size:14.5px;line-height:1.3}
.ref-btn{left:166px;top:1356px;width:199px;height:50px;background:#fff;color:var(--blue);font-weight:700;font-size:15px;display:flex;align-items:center;justify-content:space-between;padding:0 22px 0 25px;clip-path:polygon(0 0,100% 0,99% 100%,0 100%)}
.quote{left:878px;top:1230px;width:310px;color:#fff;font-size:13px;line-height:1.3;text-align:justify}
.quote-mark{color:#fff;font-size:32px;font-weight:700}
.quote-by{left:1000px;top:1357px;width:189px;text-align:right;color:#fff;font-size:12px;line-height:1.3}
.quote-by b{font-weight:700}

/* map */
.map-card{left:137px;top:1448px;width:1166px;height:330px;background:#fff}
.map{left:149px;top:1464px;width:1140px;height:299px;background:linear-gradient(120deg,#e7e7e5 0%,#eceae6 45%,#e4e6e8 100%)}

/* contact */
.contact-title{left:179px;top:1797px}
.contact-title h2{font-size:30px;font-weight:700;color:var(--blue)}
.contact-title .sub{font-size:17px;color:var(--blue)}
.contact-title p{font-size:13px;width:440px;margin-top:16px;line-height:1.32;text-align:justify}
.contact-btn{left:179px;top:1960px;width:199px;height:50px;padding:0 24px;font-size:15px;justify-content:space-between}
.cinfo{color:var(--blue)}
.cinfo b{display:block;font-size:15px;font-weight:600}
.cinfo span{font-size:23px;font-weight:400}

/* footer */
.footer{left:0;top:2075px;width:1440px;height:117px;background:var(--footer)}
.foot-mark{left:167px;top:2102px;width:64px;height:64px;border-radius:50%;border:3px solid var(--blue)}
.foot-text{left:247px;top:2111px;font-size:11.5px;line-height:1.45;color:var(--text)}
.foot-text .links{color:var(--blue)}
</style>
</head>
<body>
<div class="page">

  <svg class="header-shape" width="1440" height="125" viewBox="0 0 1440 125" aria-hidden="true">
    <path d="M440 47 H1440 V125 H0 V118 H410 Z" fill="#1b5a8c"/>
    <path d="M0 113 H412 L442 50 H1440" fill="none" stroke="#1b5a8c" stroke-width="2"/>
  </svg>

  <div class="abs brand">
    <div class="brand-mark"></div>
    <div>
      <div class="brand-name">Birke Werkstatt</div>
      <div class="brand-tag">GfK Formteile | Ur-Modellbau | Prototyping</div>
    </div>
  </div>

  <div class="abs phone-top"><b>Telefon</b>+49 (0) 321 / 480 27 16</div>

  <div class="abs meta">
    <span class="flag"></span><span>deutsch</span>|<strong>Sprache wechseln ▾</strong>
    <span style="width:14px"></span>
    <span class="lnk">Impressum</span>|<span class="lnk">Allgemeine Geschäftsbedingungen</span>
  </div>

  <nav class="abs nav">
    <a class="active">Startseite</a>
    <a>Über uns</a>
    <a>Luftfahrt / Triebwerke</a>
    <a>Formbauteile</a>
    <a>Dekoration &amp; Kunstfelsen</a>
    <a>Reparaturservice</a>
    <a>Kontakt</a>
  </nav>

  <div class="abs hero" role="img" aria-label="Verkehrsflugzeug am Flughafen mit Triebwerk-Abdeckung unter bewölktem Himmel"></div>

  <div class="abs hero-title">
    <div class="l1">Langlebige <b>Abdeckungen</b></div>
    <div class="l2">für zivile Luftfahrzeug-Triebwerke</div>
    <div class="l3">Vorne + Hinten</div>
  </div>

  <a class="abs hero-btn">
    <svg width="28" height="28" viewBox="0 0 28 28" aria-hidden="true"><circle cx="14" cy="15" r="11" fill="none" stroke="#1b5a8c" stroke-width="1.6"/><path d="M14 2v3M14 15l4-3" stroke="#1b5a8c" stroke-width="1.6" fill="none"/></svg>
    Triebwerk-Abdeckungen
    <svg width="10" height="12" viewBox="0 0 10 12" aria-hidden="true"><path d="M3 2l4 4-4 4" stroke="#1b5a8c" stroke-width="2" fill="none"/></svg>
  </a>

  <div class="abs dots"><i class="on"></i><i></i><i></i></div>
  <div class="abs arrows"><span>‹</span><span>›</span></div>

  <div class="abs submenu">
    <div class="head">Untermenü</div>
    <a>Triebwerk-Abdeckungen<span>›</span></a>
    <a>Aufblasbare Abdeckungen<span>›</span></a>
    <a>Luftfahrt-Formbauteile<span>›</span></a>
  </div>

  <section class="abs intro">
    <h2>Seit über 20 Jahren</h2>
    <div class="sub">Qualität. Kompetenz. Zuverlässig.</div>
    <p>Lorem ipsum dolor sit amet, consetetur sadipscing elitr, sed diam nonumy eirmod tempor invidunt ut labore et dolore magna aliquyam erat, sed diam voluptua. At vero eos et accusam et justo duo dolores et ea rebum.</p>
  </section>

  <div class="abs step" style="left:144px">
    <div class="ico">
      <span class="num" style="left:84px">1.</span>
      <svg class="abs" style="left:118px;top:2px" width="68" height="80" viewBox="0 0 68 80" aria-hidden="true">
        <path d="M10 62 L48 24 L58 34 L20 72 L8 74 Z M44 28 L54 38" fill="none" stroke="#1b5a8c" stroke-width="2.5"/>
      </svg>
    </div>
    <h3>Beratung &amp; Entwurf</h3>
    <p>Lorem ipsum dolor sit amet, consetetur sadipscing elitr, sed diam nonumy eirmod tempor invidunt ut labore et dolore magna aliquyam erat, sed diam voluptua. At vero eos et accusam et justo duo dolores et ea rebum.</p>
  </div>

  <div class="abs step" style="left:570px">
    <div class="ico">
      <span class="num" style="left:84px">2.</span>
      <svg class="abs" style="left:114px;top:14px" width="70" height="70" viewBox="0 0 70 70" aria-hidden="true">
        <g fill="none" stroke="#1b5a8c" stroke-width="2.5">
          <path d="M5 50 L35 35 L65 45 L35 65 Z"/>
          <path d="M5 36 L35 21 L65 31 L35 51 Z" fill="#fff"/>
          <path d="M5 20 L35 5 L65 15 L35 35 Z" fill="#fff"/>
        </g>
      </svg>
    </div>
    <h3>Material &amp; Formenbau</h3>
    <p>Lorem ipsum dolor sit amet, consetetur sadipscing elitr, sed diam nonumy eirmod tempor invidunt ut labore et dolore magna aliquyam erat, sed diam voluptua. At vero eos et accusam et justo duo dolores et ea rebum.</p>
  </div>

  <div class="abs step" style="left:1006px">
    <div class="ico">
      <span class="num" style="left:83px">3.</span>
      <svg class="abs" style="left:112px;top:14px" width="70" height="70" viewBox="0 0 70 70" aria-hidden="true">
        <g fill="none" stroke="#1b5a8c" stroke-width="2.5">
          <rect x="10" y="2" width="50" height="38"/>
          <path d="M27 10h16"/>
          <rect x="2" y="46" width="66" height="20" rx="10"/>
          <circle cx="14" cy="56" r="5"/><circle cx="35" cy="56" r="5"/><circle cx="56" cy="56" r="5"/>
        </g>
      </svg>
    </div>
    <h3>Prototyp &amp; Fertigung</h3>
    <div class="tag">Vorserie - Kleinserie - Serienfertigung</div>
    <p>Lorem ipsum dolor sit amet, consetetur sadipscing elitr, sed diam nonumy eirmod tempor invidunt ut labore et dolore magna aliquyam erat, sed diam voluptua. At vero eos et accusam et justo duo dolores et ea rebum.</p>
  </div>

  <a class="abs btn-dark about-btn">Über uns<small>Mehr erfahren</small>›</a>

  <div class="abs band" role="img" aria-label="Collage von Referenzprojekten in blauer Tönung"></div>

  <div class="abs band-title">Unsere Kunden vertrauen<br>auf unsere <b>Qualität</b>.</div>
  <p class="abs band-text">Wir sind stolz auf unsere Referenzen und die stetige Zufriedenheit unserer Kunden seit über 20 Jahren. Überzeugen Sie sich von unseren Werken in unserer Referenz-Galerie.</p>
  <a class="abs ref-btn">Referenzen<span>›</span></a>

  <span class="abs quote-mark" style="left:1192px;top:1212px">“</span>
  <p class="abs quote">Lorem ipsum dolor sit amet, consetetur sadipscing elitr, sed diam nonumy eirmod tempor invidunt ut labore et dolore magna aliquyam erat, sed diam voluptua. At vero eos et accusam et justo duo dolores et ea rebum. Stet clita kasd gubergren, no sea takimata sanctus est Lorem ipsum dolor sit amet.</p>
  <span class="abs quote-mark" style="left:850px;top:1327px">”</span>
  <div class="abs quote-by"><b>Jonas Feldberg</b><br>Nordluft Technik GmbH</div>

  <div class="abs map-card"></div>
  <div class="abs map" role="img" aria-label="Stadtplan mit Standortmarkierung der Werkstatt"></div>

  <div class="abs contact-title">
    <h2>Haben Sie Interesse?</h2>
    <div class="sub">Zögern Sie bitte nicht uns zu kontaktieren.</div>
    <p>Lorem ipsum dolor sit amet, consetetur sadipscing elitr, sed diam nonumy eirmod tempor invidunt ut labore et dolore magna aliquyam erat, sed diam voluptua. At vero eos et accusam et justo duo dolores et ea rebum.</p>
  </div>
  <a class="abs btn-dark contact-btn">Referenzen<span>›</span></a>

  <div class="abs cinfo" style="left:688px;top:1828px"><b>Telefon</b><span>+49 (0) 321 / 480 27 16</span></div>
  <div class="abs cinfo" style="left:970px;top:1828px"><b>E-Mail</b><span>info[at]birke-werkstatt.de</span></div>
  <div class="abs cinfo" style="left:688px;top:1901px"><b>Fax</b><span>+49 (0) 321 / 480 27 15</span></div>

  <footer class="abs footer"></footer>
  <div class="abs foot-mark"></div>
  <div class="abs foot-text">
    Copyright @ 2017 Birke Werkstatt<br>
    <span class="links">Impressum &nbsp;|&nbsp; Allgemeine Geschäftsbedingungen &nbsp;|&nbsp; Kontakt</span>
  </div>

</div>
</body>
</html>
```